Business Card Design Project

Hi
I'm currently getting a logo designed which will go on the front. It is designed for s
Fitness instructor/ personal training business.
On the back I would like written:
Boxing for Fitness
Aqua Fitness Professional
PersonalisedTraining 1/1 or Small Group outdoor training
Fun and unique workouts
Weight loss/ Strength training

Also I need on there my details
minaharper27@quillbox.net
0427 395 108
FB Mina Motion

Reason: I would like to extend the deadline to give extra days after I have confirmed the logo in two days

Target Market(s)

Mostly women aged between 20-50

Industry/Entity Type

Training

Font styles to use
Sans Serif

Requirements
Must have
• My logo ( I have attached my favourite logo options )
My details

```html
<!DOCTYPE html>
<html lang="en">
<head>
<meta charset="utf-8">
<title>Mina Motion – Business Cards</title>
<link rel="stylesheet" href="https://fonts.googleapis.com/css2?family=Jost:wght@500;600&display=swap">
<style>
  :root {
    --canvas: #f4f4f3;
    --card-blue: #0a76dc;
    --card-grey: #e4e4e1;
    --brand-blue: #0a76dc;
    --ink-dark: #111111;
    --ink-orange: #f08a2c;
    --ink-light: #ffffff;
  }
  * { box-sizing: border-box; margin: 0; padding: 0; }
  html, body { width: 1200px; height: 1000px; overflow: hidden; }
  body {
    background: var(--canvas);
    font-family: "Jost", "Futura", sans-serif;
  }
  .card-set {
    position: absolute;
    left: 60px;
    display: flex;
    gap: 40px;
  }
  .card-set--dark { top: 70px; }
  .card-set--orange { top: 530px; }

  .card {
    position: relative;
    width: 520px;
    height: 297px;
    border-radius: 3px;
    box-shadow: 0 10px 24px rgba(0,0,0,0.12);
    overflow: hidden;
  }

  /* Back of card */
  .card-back { background: var(--card-blue); color: var(--ink); }
  .card-set--dark .card-back { --ink: var(--ink-dark); }
  .card-set--orange .card-back { --ink: var(--ink-orange); }

  .specialties {
    position: absolute;
    left: 34px;
    top: 34px;
    border: 2px solid var(--ink);
    padding: 6px 14px 6px 10px;
    font-weight: 600;
    font-size: 19px;
    line-height: 1.2;
  }
  .services {
    position: absolute;
    left: 28px;
    top: 112px;
    list-style: none;
    font-weight: 500;
    font-size: 19px;
    line-height: 1.2;
    width: 380px;
  }
  .services li::before { content: "•"; }

  .mini-brand {
    position: absolute;
    right: 22px;
    top: 108px;
    display: flex;
    align-items: center;
    gap: 5px;
    color: var(--ink-light);
    font-weight: 600;
    font-size: 13px;
  }
  .mini-brand .dot {
    width: 10px; height: 10px;
    border-radius: 50%;
    background: var(--ink-light);
  }
  .contact {
    position: absolute;
    right: 18px;
    bottom: 22px;
    writing-mode: vertical-rl;
    color: var(--ink-light);
    font-weight: 500;
    font-size: 11px;
    line-height: 1.35;
  }

  /* Front of card */
  .card-front {
    background: var(--card-grey);
    display: flex;
    align-items: center;
    justify-content: center;
    gap: 16px;
  }
  .brand-circle {
    width: 56px; height: 56px;
    border-radius: 50%;
    border: 4px solid var(--brand-blue);
  }
  .brand-name {
    color: var(--brand-blue);
    font-weight: 600;
    font-size: 54px;
    letter-spacing: 0.5px;
  }
</style>
</head>
<body>

<section class="card-set card-set--dark">
  <article class="card card-back">
    <div class="specialties">Boxing for Fitness<br>Aqua Fitness Professional</div>
    <ul class="services">
      <li>PersonalisedTraining 1/1 or Small Group outdoor training</li>
      <li>Fun and unique workouts</li>
      <li>Weight loss/ Strength training</li>
    </ul>
    <div class="mini-brand"><span class="dot"></span>Mina Motion</div>
    <div class="contact">minaharper27@quillbox.net<br>0427 395 108<br>FB Mina Motion</div>
  </article>
  <article class="card card-front">
    <span class="brand-circle"></span>
    <span class="brand-name">Mina Motion</span>
  </article>
</section>

<section class="card-set card-set--orange">
  <article class="card card-back">
    <div class="specialties">Boxing for Fitness<br>Aqua Fitness Professional</div>
    <ul class="services">
      <li>PersonalisedTraining 1/1 or Small Group outdoor training</li>
      <li>Fun and unique workouts</li>
      <li>Weight loss/ Strength training</li>
    </ul>
    <div class="mini-brand"><span class="dot"></span>Mina Motion</div>
    <div class="contact">minaharper27@quillbox.net<br>0427 395 108<br>FB Mina Motion</div>
  </article>
  <article class="card card-front">
    <span class="brand-circle"></span>
    <span class="brand-name">Mina Motion</span>
  </article>
</section>

</body>
</html>
```